Harborlight Capital Estates business card

We are a real estate advisory and investment company. We are specialized in assisting high networth individuals to invest in real estate overseas. We deliver a very personalized service, anticipating all the potential challenges an investor can face, and making it easy and safe for them. We also co-invest with our clients, assuring them that each project will be looked after as it is our own, and at the same time giving them the extra booth on confidence to invest.

We need a business card design. The business card must have a very premium, high-end look, reflecting principles like "commitment", "trust" and "timeless (but contemporary)". We look for long term relationships with our clients, and we grow with their referrals. We are all about conquering the confidence of the clients by always delivering above the expectations performance.

Target Market(s)

High net worth individuals.

Industry/Entity Type

Real Estate

Contact Information for Business Card

Please consider places on the business card for:

Name
Function (bellow name in smaller size text)

Mobile phone
E-mail
Voice ID
Chat ID

Adress (3 lines)

Also include the following locations references:
PORTUGAL * DUBAI * HONG KONG

Website: www.hcestates-example.com

Requirements
Must have
• Company Logo

```html
<!DOCTYPE html>
<html lang="en">
<head>
<meta charset="utf-8">
<title>Harborlight Capital Estates – Business Card</title>
<link rel="stylesheet" href="https://fonts.googleapis.com/css2?family=Arimo:wght@400;700&display=swap">
<style>
  :root {
    --backdrop: #e7e9ec;
    --card-blue-start: #3a97dd;
    --card-blue-end: #6cbcec;
    --card-white: #ffffff;
    --brand-blue: #3fa5e2;
    --ink: #6a6d72;
    --ink-strong: #55585d;
    --rule: #c9ccd0;
    --white: #ffffff;
  }
  * { box-sizing: border-box; margin: 0; padding: 0; }
  html, body {
    width: 1200px; height: 712px; overflow: hidden;
    background: var(--backdrop);
    font-family: "Arimo", Arial, sans-serif;
  }
  .stage {
    position: relative; width: 1200px; height: 712px;
    display: flex; align-items: center; justify-content: center; gap: 50px;
  }
  .card {
    width: 525px; height: 300px; position: relative;
    box-shadow: 0 6px 18px rgba(0,0,0,0.12);
  }

  /* Front */
  .card-front {
    background: linear-gradient(135deg, var(--card-blue-start), var(--card-blue-end));
    color: var(--white);
    display: flex; flex-direction: column; align-items: center; justify-content: center;
  }
  .front-brand {
    font-weight: 700; font-size: 27px; letter-spacing: 1.5px; text-transform: uppercase;
    text-align: center; line-height: 1.2; color: var(--white);
  }
  .front-brand .brand-sub { display: block; font-size: 14px; letter-spacing: 5px; }
  .front-rule { width: 250px; height: 1px; background: var(--white); margin: 12px 0 10px; opacity: .9; }
  .locations { font-size: 10px; letter-spacing: 1.5px; }
  .locations .dot { margin: 0 8px; }

  /* Back */
  .card-back { background: var(--card-white); color: var(--ink); }
  .back-brand {
    position: absolute; left: 34px; top: 40px;
    display: flex; align-items: center; gap: 10px;
    color: var(--brand-blue); font-weight: 700; text-transform: uppercase;
  }
  .back-brand .mark { width: 12px; height: 12px; border-radius: 50%; background: var(--brand-blue); }
  .back-brand .brand-name { font-size: 20px; letter-spacing: 1px; line-height: 1.15; }
  .back-brand .brand-sub { display: block; font-size: 11px; letter-spacing: 3.5px; }
  .person { position: absolute; left: 34px; top: 128px; }
  .person-name { font-weight: 700; font-size: 14px; color: var(--ink-strong); letter-spacing: .5px; }
  .person-role { font-size: 11px; color: var(--brand-blue); margin-top: 3px; }
  .address { font-size: 11px; line-height: 1.45; margin-top: 12px; font-style: normal; }
  .divider { position: absolute; left: 292px; top: 160px; width: 1px; height: 100px; background: var(--rule); }
  .contacts { position: absolute; left: 306px; top: 160px; list-style: none; font-size: 11px; }
  .contacts li { display: flex; align-items: center; height: 19px; }
  .contacts .label {
    width: 42px; color: var(--brand-blue); font-weight: 700; font-size: 10px;
    display: flex; align-items: center;
  }
  .contacts svg { width: 12px; height: 12px; fill: none; stroke: var(--rule); stroke-width: 1.6; }
</style>
</head>
<body>
<main class="stage">
  <section class="card card-front" aria-label="Card front">
    <h1 class="front-brand">Harborlight<span class="brand-sub">Capital Estates</span></h1>
    <div class="front-rule"></div>
    <p class="locations">PORTUGAL<span class="dot">•</span>DUBAI<span class="dot">•</span>HONG KONG</p>
  </section>

  <section class="card card-back" aria-label="Card back">
    <div class="back-brand">
      <span class="mark"></span>
      <span class="brand-name">Harborlight<span class="brand-sub">Capital Estates</span></span>
    </div>

    <div class="person">
      <p class="person-name">DANIEL CARVER</p>
      <p class="person-role">Business Manager</p>
      <address class="address">Level 12 Beacon<br>Harbour View Lane<br>Suite 4410</address>
    </div>

    <div class="divider"></div>

    <ul class="contacts">
      <li><span class="label"><svg viewBox="0 0 12 12"><rect x="3" y="1" width="6" height="10" rx="1"/></svg></span>0400 555 018</li>
      <li><span class="label"><svg viewBox="0 0 12 12"><rect x="1" y="2.5" width="10" height="7"/><path d="M1 2.5l5 4 5-4"/></svg></span>info@hcestates-example.com</li>
      <li><span class="label"><svg viewBox="0 0 12 12"><circle cx="6" cy="6" r="5"/><path d="M1 6h10M6 1c-3 3-3 7 0 10M6 1c3 3 3 7 0 10"/></svg></span>www.hcestates-example.com</li>
      <li><span class="label">Voice</span>hcestates.advisory</li>
      <li><span class="label">Chat</span>hcestates07</li>
    </ul>
  </section>
</main>
</body>
</html>
```